Flyer Design Project

We need a flyer for a monthly event that we will be having. The flyer needs to be editable in either adobe illustrator or photoshop so that we can change the details such as the date if needed... Preferable in vector art.

Name of Event : Sandalmania

Price of Tickets: $15 Tickets- Entry fee ensures a pair of thongs upon leaving, drink specials all night and priority entry.

WHEN- FEB 20th
WHERE- Velvet Loft
DJ: Tessa Harlow
web: www.velvetloftbar.com.au
ph: 9146 3705

Drink specials from 7-9pm
$3 Pots
$4 basics
$4 kelvanos

$1 pizza from 8pm-10pm

FREE PAIR OF THONGS ON DEPARTURE

Drink specials continue throughout the night

Open 7pm-3am
Updates

Hi there,

Just to be clear, a pair of thongs isĀ referringĀ to flip flops or sandals (not underwear)... thanks

Target Market(s)

University Students 18-24 years old

Industry/Entity Type

Apartment

Requirements
Must have
• must have our logo

```html
<!DOCTYPE html>
<html lang="en">
<head>
<meta charset="utf-8">
<title>Sandalmania – Velvet Loft</title>
<link rel="stylesheet" href="https://fonts.googleapis.com/css2?family=Titan+One&family=Jost:wght@300;400;600;700&display=swap">
<style>
  :root {
    --page-bg: #e4e4e2;
    --paper: #fdf1dd;
    --orange: #e0601a;
    --ink: #111111;
    --band-yellow: #f8c86a;
    --white: #ffffff;
    --sandal-green: #9bc43c;
    --sandal-yellow: #f4d93a;
    --sandal-red: #e2321e;
  }
  * { margin: 0; padding: 0; box-sizing: border-box; }
  html, body {
    width: 1200px; height: 900px; overflow: hidden;
    background: var(--page-bg);
  }
  .flyer {
    position: absolute; left: 20px; top: 30px;
    width: 1160px; height: 840px;
    background: var(--paper);
    border: 1px solid #3a3a3a;
    overflow: hidden;
    font-family: "Jost", "Century Gothic", sans-serif;
    color: var(--ink);
  }
  .sandals-art {
    position: absolute; left: 0; top: 0; width: 500px; height: 760px;
  }
  .sandal {
    position: absolute;
    border-radius: 48% 48% 44% 44% / 30% 30% 24% 24%;
    background: linear-gradient(170deg, var(--sandal-yellow) 0%, var(--sandal-green) 35%, var(--orange) 70%, var(--sandal-red) 100%);
    opacity: 0.85;
  }
  .sandal.left  { left: 58px;  top: 94px;  width: 182px; height: 482px; transform: rotate(-3deg); }
  .sandal.right { left: 232px; top: 276px; width: 228px; height: 452px; transform: rotate(6deg); }
  .venue-name {
    position: absolute; left: 420px; top: 36px;
    display: flex; align-items: center; gap: 14px;
    font-family: "Titan One", sans-serif;
    font-size: 40px; line-height: 1; color: var(--ink);
  }
  .venue-name .dot {
    width: 18px; height: 18px; border-radius: 50%; background: var(--ink);
  }
  .event-title {
    position: absolute; right: 56px; top: 104px;
    font-family: "Titan One", sans-serif;
    font-size: 104px; line-height: 1.1; letter-spacing: 1px;
    color: var(--orange);
    text-shadow: 6px 6px 0 var(--ink);
  }
  .event-date {
    position: absolute; right: 60px; top: 222px;
    font-weight: 700; font-size: 50px; line-height: 1.2;
  }
  .event-hours {
    position: absolute; right: 60px; top: 290px;
    font-weight: 400; font-size: 30px; line-height: 1.2;
  }
  .specials-band {
    position: absolute; left: 533px; right: 0; top: 347px; height: 234px;
    background: var(--orange);
    color: var(--white);
    padding: 18px 0 0 46px;
  }
  .specials-band p { line-height: 1; white-space: nowrap; }
  .specials-band p + p { margin-top: 24px; }
  .specials-band strong { font-weight: 700; font-size: 48px; }
  .specials-band span { font-weight: 300; font-size: 28px; margin-left: 6px; margin-right: 4px; }
  .tickets {
    position: absolute; left: 639px; width: 400px; top: 598px;
    text-align: center;
    font-family: "Titan One", sans-serif;
    font-size: 56px; line-height: 1.2; color: var(--orange);
    text-shadow: 3px 3px 0 var(--ink);
  }
  .ticket-perk {
    position: absolute; left: 540px; width: 600px; text-align: center;
    font-weight: 700; line-height: 1.2;
  }
  .ticket-perk.main { top: 677px; font-size: 26px; }
  .ticket-perk.note { top: 714px; font-size: 21px; }
  .contact-band {
    position: absolute; left: 0; right: 0; bottom: 0; height: 74px;
    background: var(--band-yellow);
    display: flex; align-items: center; justify-content: flex-end;
    padding-right: 66px;
    font-size: 27px; font-weight: 400; white-space: nowrap;
  }
  .contact-band strong { font-weight: 700; }
</style>
</head>
<body>
  <main class="flyer">
    <div class="sandals-art" role="img" aria-label="Illustration of a pair of striped flip-flop sandals with red straps">
      <div class="sandal left"></div>
      <div class="sandal right"></div>
    </div>

    <div class="venue-name"><span class="dot"></span>Velvet Loft</div>

    <h1 class="event-title">Sandalmania</h1>
    <p class="event-date">FEB 20th</p>
    <p class="event-hours">Open 7pm-3am</p>

    <section class="specials-band">
      <p><strong>Drink specials</strong><span>from 7-9pm</span></p>
      <p><strong>$3</strong><span>Pots</span><strong>$4</strong><span>basics</span><strong>$4</strong><span>kelvanos</span></p>
      <p><strong>$1 Pizza</strong><span>from 8pm-10pm</span></p>
    </section>

    <p class="tickets">$15 Tickets</p>
    <p class="ticket-perk main">FREE PAIR OF THONGS ON DEPARTURE</p>
    <p class="ticket-perk note">Drink specials continue throughout the night</p>

    <footer class="contact-band">
      <p><strong>DJ: Tessa Harlow,</strong>&nbsp;web: www.velvetloftbar.com.au, phone: 9146 3705</p>
    </footer>
  </main>
</body>
</html>
```